Business Card Design Project

Need business card for new non profit organization that includes the attached logo in some form.
with this information
Name: Michael Dorrance Pilbeam
Title: President & Founder
A: P.O. Box 51607, Portland, Oregon, 97214-5160
E: mike@dorrancetrust.org
E: mike@mikepilbeam.com
P: 1.971.555.0172

Industry/Entity Type
Non Profit

```html
<!DOCTYPE html>
<html lang="en">
<head>
<meta charset="utf-8">
<title>Dorrance Trust – Business Card</title>
<link rel="stylesheet" href="https://fonts.googleapis.com/css2?family=Montserrat:wght@700&family=Arimo:wght@400;700&family=Noto+Serif:wght@700&display=swap">
<style>
  :root {
    --orange: #ff7800;
    --black: #0c0c0c;
    --steel-dark: #242424;
    --steel-light: #4a4a4a;
    --white: #ffffff;
    --rule-grey: #8c8c8c;
    --panel-grey: #6b6b6b;
    --navy: #1c2f6e;
    --phone-bg: #4c4c4c;
  }
  html, body {
    margin: 0;
    padding: 0;
    width: 1200px;
    height: 800px;
    overflow: hidden;
    background: var(--white);
  }
  .card {
    position: relative;
    width: 1200px;
    height: 800px;
    overflow: hidden;
    background: var(--black);
  }
  .card-shapes {
    position: absolute;
    inset: 0;
  }
  .title-band {
    position: absolute;
    left: 0; top: 0;
    width: 1200px; height: 155px;
    background: var(--orange);
    display: flex;
    align-items: center;
    justify-content: center;
  }
  .title {
    margin: 0;
    font-family: "Montserrat", Arial, sans-serif;
    font-weight: 700;
    font-size: 62px;
    color: var(--white);
    letter-spacing: 0.5px;
  }
  .name {
    position: absolute;
    left: 12px; top: 318px;
    margin: 0;
    font-family: "Arimo", Arial, sans-serif;
    font-weight: 400;
    font-size: 43px;
    line-height: 54px;
    color: var(--white);
  }
  .org-mark {
    position: absolute;
    left: 650px; top: 290px;
    width: 540px; height: 260px;
    display: flex;
    align-items: center;
    justify-content: center;
    gap: 22px;
  }
  .org-mark__square {
    width: 70px; height: 70px;
    background: var(--navy);
  }
  .org-mark__name {
    font-family: "Noto Serif", Georgia, serif;
    font-weight: 700;
    font-size: 48px;
    color: var(--navy);
  }
  .contact-list {
    position: absolute;
    left: 78px; top: 628px;
    margin: 0; padding: 0;
    list-style: none;
    font-family: "Noto Serif", Georgia, serif;
    font-weight: 700;
    font-size: 30px;
    color: var(--white);
  }
  .contact-list li {
    display: flex;
    align-items: center;
    height: 48px;
  }
  .contact-icon {
    width: 42px;
    display: inline-flex;
    justify-content: flex-start;
    font-family: "Arimo", Arial, sans-serif;
    font-size: 36px;
  }
  .ornament {
    position: absolute;
    left: 1010px; top: 568px;
    width: 190px; height: 170px;
    background: radial-gradient(ellipse at 55% 50%, rgba(232,120,40,0.75), rgba(46,150,70,0.45) 55%, rgba(107,107,107,0) 75%);
  }
  .phone {
    position: absolute;
    right: 0; top: 722px;
    height: 72px;
    padding: 0 16px 0 798px;
    display: flex;
    align-items: center;
    gap: 12px;
    font-family: "Arimo", Arial, sans-serif;
    font-weight: 700;
    font-size: 38px;
    color: var(--white);
    letter-spacing: 1px;
  }
</style>
</head>
<body>
<main class="card">
  <svg class="card-shapes" width="1200" height="800" viewBox="0 0 1200 800" aria-hidden="true">
    <defs>
      <linearGradient id="steel" x1="0" y1="0" x2="1" y2="1">
        <stop offset="0" stop-color="#1e1e1e"/>
        <stop offset="0.5" stop-color="#3a3a3a"/>
        <stop offset="1" stop-color="#2a2a2a"/>
      </linearGradient>
      <linearGradient id="phone-fade" x1="0" y1="0" x2="1" y2="0">
        <stop offset="0" stop-color="#4c4c4c" stop-opacity="0"/>
        <stop offset="0.35" stop-color="#3c3c3c"/>
        <stop offset="1" stop-color="#3c3c3c"/>
      </linearGradient>
    </defs>
    <!-- dark steel field -->
    <rect class="steel-field" x="0" y="155" width="1200" height="450" fill="url(#steel)"/>
    <!-- black divider under the title band -->
    <rect x="0" y="155" width="1200" height="18" fill="var(--black)"/>
    <!-- white logo panel with diagonal edge -->
    <polygon class="logo-panel" points="718,173 1200,173 1200,580 430,580" fill="var(--white)"/>
    <!-- light grey rule -->
    <polygon points="430,580 1200,580 1200,605 414,605" fill="var(--rule-grey)"/>
    <!-- contact panel -->
    <rect class="contact-panel" x="0" y="605" width="1200" height="195" fill="var(--panel-grey)"/>
    <!-- name strip -->
    <polygon class="name-strip" points="0,318 598,318 568,372 0,372" fill="var(--black)"/>
    <!-- phone strip -->
    <rect x="780" y="722" width="420" height="72" fill="url(#phone-fade)"/>
  </svg>

  <header class="title-band">
    <h1 class="title">President &amp; Founder</h1>
  </header>

  <p class="name">Michael Dorrance Pilbeam</p>

  <div class="org-mark">
    <span class="org-mark__square"></span>
    <span class="org-mark__name">Dorrance Trust</span>
  </div>

  <ul class="contact-list">
    <li>
      <span class="contact-icon">
        <svg width="36" height="30" viewBox="0 0 36 30" aria-hidden="true">
          <path d="M2 12 L18 2 L34 12 V28 H2 Z" fill="none" stroke="#fff" stroke-width="2.5" stroke-linejoin="round"/>
          <path d="M2 12 L18 22 L34 12" fill="none" stroke="#fff" stroke-width="2.5"/>
        </svg>
      </span>
      <span>: P.O. Box 51607, Portland, Oregon, 97214-5160</span>
    </li>
    <li><span class="contact-icon">@</span><span>: mike@dorrancetrust.org</span></li>
    <li><span class="contact-icon">@</span><span>: mike@mikepilbeam.com</span></li>
  </ul>

  <div class="ornament" role="img" aria-label="Decorative swirl ornament in orange, green, pink and blue"></div>

  <div class="phone">
    <svg width="58" height="58" viewBox="0 0 58 58" aria-hidden="true">
      <circle cx="29" cy="29" r="26" fill="none" stroke="#fff" stroke-width="3"/>
      <path d="M22 16 c-4 2 -5 8 -2 15 c3 7 8 12 13 12 l3 -5 l-6 -4 l-3 3 c-3 -1 -6 -6 -6 -10 l3 -2 l-2 -8 z" fill="#fff"/>
    </svg>
    <span>: 1.971.555.0172</span>
  </div>
</main>
</body>
</html>
```